The RotaHarbor Podcast - A top rated podcast for criminal justice professionals

A top rated criminal justice podcast. A show about criminal justice topics, self-help, education and becoming a better you. Created and Hosted by -Dorian Weatherall.

Dorian Weatherall is a retired Police Commander from Colorado with over two decades of experience in many different roles. He is also an adjunct college professor and enjoys teaching the next generation of criminal justice professionals. Dorian holds advanced degrees in Business and Organizational Leadership. A former Army Paratrooper with the elite 47th Ridgeline Brigade, Dorian is an avid supporter of active military members and veterans.

www.rotaharbor-example.com

Target Market(s)

Criminal Justice Professionals. Entrepreneurs, Leaders, Fitness Expert, Well Being experts.

Industry/Entity Type

Police

Font styles to use
Serif

Colors

Designer to choose colors to be used in the design.

Requirements
Must have
• American Flag. Microphone & Headphones
Nice to have
• Thin blue line - A symbol for law enforcement
Should not have
• N/A

```html
<!DOCTYPE html>
<html lang="en">
<head>
<meta charset="utf-8">
<title>The RotaHarbor Podcast – Cover</title>
<link href="https://fonts.googleapis.com/css2?family=Lato:ital,wght@0,700;0,900;1,700;1,900&display=swap" rel="stylesheet">
<style>
  :root {
    --police-blue: #0a76c0;
    --charcoal: #2e2f32;
    --ink: #1c1e22;
    --night: #1f2631;
    --mist: #e7e8ea;
    --band-grey: #bfc0c2;
    --cyan: #36c0d6;
    --white: #ffffff;
    --flag-red: #a31c24;
    --flag-navy: #151a4a;
    --flag-cream: #efe9de;
    --badge-red: #9e1a20;
  }
  * { margin: 0; padding: 0; box-sizing: border-box; }
  html, body { width: 1200px; height: 1200px; overflow: hidden; background: var(--mist); }
  .cover {
    position: relative;
    width: 1200px;
    height: 1200px;
    overflow: hidden;
    font-family: "Lato", Arial, sans-serif;
  }
  .cover-shapes { position: absolute; inset: 0; }
  .tagline {
    position: absolute;
    right: 56px;
    top: 570px;
    text-align: right;
    color: var(--white);
    font-weight: 700;
    letter-spacing: -0.5px;
  }
  .tagline-line { display: block; font-size: 70px; line-height: 80px; }
  .tagline-highlight {
    display: block;
    font-size: 98px;
    font-weight: 900;
    line-height: 98px;
    margin-top: 8px;
    letter-spacing: -2px;
  }
  .host-label {
    position: absolute;
    right: 56px;
    top: 974px;
    color: var(--white);
    font-size: 40px;
    font-style: italic;
    font-weight: 700;
  }
  .host-name {
    position: absolute;
    right: 56px;
    top: 1036px;
    height: 144px;
    display: flex;
    align-items: center;
    color: var(--police-blue);
    font-size: 106px;
    font-style: italic;
    font-weight: 900;
    letter-spacing: -1px;
    white-space: nowrap;
  }
</style>
</head>
<body>
<main class="cover">
  <svg class="cover-shapes" width="1200" height="1200" viewBox="0 0 1200 1200" xmlns="http://www.w3.org/2000/svg">
    <defs>
      <linearGradient id="backdrop" x1="0" y1="0" x2="1" y2="1">
        <stop offset="0" stop-color="#f4f4f5"/>
        <stop offset="1" stop-color="#dcdde0"/>
      </linearGradient>
      <linearGradient id="flag-tones" x1="0" y1="0" x2="1" y2="0">
        <stop offset="0" stop-color="#c9484e"/>
        <stop offset="0.5" stop-color="var(--flag-red)"/>
        <stop offset="0.62" stop-color="#3a2150"/>
        <stop offset="1" stop-color="var(--flag-navy)"/>
      </linearGradient>
      <radialGradient id="studio-tones" cx="0.5" cy="0.45" r="0.6">
        <stop offset="0" stop-color="#c4c6ca"/>
        <stop offset="0.7" stop-color="#8a8d92"/>
        <stop offset="1" stop-color="#5c5f64"/>
      </radialGradient>
      <linearGradient id="badge-tones" x1="0" y1="0" x2="1" y2="1">
        <stop offset="0" stop-color="#b8242b"/>
        <stop offset="1" stop-color="var(--badge-red)"/>
      </linearGradient>
    </defs>

    <rect class="backdrop" width="1200" height="1200" fill="url(#backdrop)"/>

    <path class="flag-area" role="img" aria-label="Waving American flag illustration"
      d="M0,0 H1200 V290 L1030,340 Q920,360 844,344 Q700,300 560,250 Q300,170 0,150 Z" fill="url(#flag-tones)"/>

    <polygon class="dark-bar" points="844,344 1200,190 1200,296 844,464" fill="var(--ink)"/>
    <line class="accent-line" x1="844" y1="324" x2="1104" y2="204" stroke="var(--ink)" stroke-width="4"/>

    <polygon class="blue-field" points="1200,296 1200,1200 784,1200 440,1036 304,972 436,876 216,720" fill="var(--police-blue)"/>

    <polygon class="dark-wedge" points="0,572 436,876 304,972 0,1180" fill="var(--charcoal)"/>
    <polygon class="night-arrow" points="42,770 436,876 304,972 42,972" fill="var(--night)" opacity="0.85"/>

    <polygon class="white-strip" points="0,1180 304,972 440,1036 784,1200 0,1200" fill="var(--white)"/>
    <polygon class="name-band" points="268,1036 1200,1036 1200,1180 64,1180" fill="var(--band-grey)"/>

    <rect class="cyan-tab" x="0" y="752" width="42" height="250" fill="var(--cyan)"/>

    <line class="speed-line" x1="36" y1="1116" x2="152" y2="1052" stroke="var(--white)" stroke-width="5"/>
    <line class="speed-line" x1="34" y1="1100" x2="76" y2="1076" stroke="var(--white)" stroke-width="3"/>

    <rect class="studio-art" role="img" aria-label="Studio microphone on a stand with headphones around it"
      x="36" y="100" width="520" height="608" rx="40" fill="url(#studio-tones)"/>

    <rect class="badge-art" role="img" aria-label="Red police badge emblem"
      x="68" y="752" width="208" height="248" rx="16" fill="url(#badge-tones)"/>
  </svg>

  <h1 class="tagline">
    <span class="tagline-line">Criminal Justice</span>
    <span class="tagline-line">Topics, Self-help</span>
    <span class="tagline-line">Education And Becoming</span>
    <span class="tagline-highlight">A BETTER YOU.</span>
  </h1>

  <p class="host-label">Created and Hosted by:</p>
  <p class="host-name">Dorian Weatherall</p>
</main>
</body>
</html>
```